Games in Classrooms Sponsorship Brochure

We need a 4 page sponsorship booklet designed for Games in Classrooms. Games in Classrooms is a scheme that brings top GB athletes into primary schools to encourage children to lead a healthy life and raise much needed funds for schools to buy new sports equipment. We would like to see designs that are eye catching, colourful and would appeal to children. I have attached the Young Hearts Appeal Fundraising Pack (FULL PACK) for design ideas and a Word Document containing potential content (Sponsorship Form - Generic.docx) . I have also attached our brand guidelines and colour palette (Brand Guidelines PPT). WE would like to see pictures of our events and athletes to help bring the sponsorship form to life. I have attached some examples but please feel free to ask for more.

Target Market(s)

Children/Parents and Families/Friends

Requirements
Must have
• 4 pages
• Be a booklet
• Have a sponsorship form on the front
• Be eye catching
• Be colourful

```html
<!DOCTYPE html>
<html lang="en">
<head>
<meta charset="utf-8">
<title>Games in Classrooms – My Sponsorship Form</title>
<link rel="stylesheet" href="https://fonts.googleapis.com/css2?family=Montserrat:wght@600;700&family=Open+Sans:wght@400;600&family=Oswald:wght@400&family=Fredoka:wght@500;600&display=swap">
<style>
  :root {
    --backdrop: #e6e8ea;
    --paper: #ffffff;
    --ink: #2f2f2f;
    --brand-red: #e2262d;
    --brand-orange: #e85a2e;
    --brand-blue: #0a97d9;
    --brand-green: #4aab3d;
    --table-green: #6cb33f;
    --table-orange: #ea5b2b;
    --table-red: #dd2b37;
    --field-grey: #ececec;
    --cell-light: #efefef;
    --cell-mid: #d9d9d9;
    --cell-dark: #cfcfcf;
    --partner-purple: #7b3a93;
    --partner-green: #2c8a3c;
  }
  * { box-sizing: border-box; margin: 0; padding: 0; }
  html, body { width: 1200px; height: 1200px; overflow: hidden; background: var(--backdrop); }
  .form-page {
    position: absolute; left: 180px; top: 6px;
    width: 918px; height: 1298px;
    background: var(--paper);
    transform: scale(0.915); transform-origin: top left;
    font-family: "Open Sans", sans-serif; color: var(--ink);
  }
  .form-page > * { position: absolute; }

  .brand { left: 280px; top: 110px; display: flex; align-items: center; gap: 14px; }
  .brand-dot { width: 62px; height: 62px; border-radius: 50%; background: var(--brand-blue); }
  .brand-name { font-family: "Montserrat", sans-serif; font-weight: 700; font-size: 30px; color: var(--ink); }

  .field { width: 256px; }
  .field-label {
    height: 44px; border-radius: 22px; color: #fff;
    font-family: "Oswald", sans-serif; font-size: 29px; line-height: 44px;
    padding-left: 26px; text-transform: uppercase; letter-spacing: 0.5px;
  }
  .field-input {
    margin-top: 10px; height: 41px; border-radius: 21px; background: var(--field-grey);
    font-size: 18px; line-height: 38px; padding-left: 26px; letter-spacing: 1px; color: #333;
  }
  .field-input .currency { color: var(--brand-green); font-weight: 600; font-size: 24px; margin-right: 14px; }
  .field--name { left: 53px; top: 233px; }
  .field--name .field-label { background: var(--brand-orange); }
  .field--class { left: 332px; top: 233px; }
  .field--class .field-label { background: var(--brand-blue); }
  .field--raised { left: 610px; top: 233px; }
  .field--raised .field-label { background: var(--brand-green); }

  .form-title {
    left: 53px; top: 358px; width: 813px; text-align: center;
    font-family: "Montserrat", sans-serif; font-weight: 700; font-size: 37px;
    color: var(--brand-red); letter-spacing: 1px;
  }
  .title-rule { left: 53px; top: 409px; width: 813px; height: 2px; background: var(--brand-red); }

  .intro { left: 53px; top: 424px; width: 813px; font-size: 18px; line-height: 26px; }
  .intro p { margin-bottom: 25px; }

  .milestone { top: 598px; width: 200px; height: 190px; }
  .milestone--one { left: 53px; }
  .milestone--two { left: 281px; }
  .milestone--three { left: 508px; }
  .milestone-badge {
    position: absolute; left: 0; top: 0; width: 125px; height: 125px; border-radius: 50%;
    background: var(--brand-blue); color: #fff; text-align: center;
    font-family: "Fredoka", sans-serif; font-weight: 600;
  }
  .milestone-badge .raise { display: block; font-size: 28px; line-height: 26px; margin-top: 18px; }
  .milestone-badge .over { display: block; font-size: 21px; line-height: 16px; }
  .milestone-badge .amount { display: block; font-size: 48px; line-height: 48px; }
  .wristbands {
    position: absolute; left: 36px; top: 114px; width: 164px; height: 74px; border-radius: 37px;
    background: linear-gradient(100deg, #4b4ea3 0%, #4b4ea3 50%, #c8352a 52%, #c8352a 100%);
  }

  .plus { left: 712px; top: 722px; font-size: 44px; font-weight: 400; line-height: 44px; color: #222; }
  .booklet-cover {
    left: 756px; top: 625px; width: 110px; height: 160px;
    background: linear-gradient(150deg, #d9dfea 0%, #c73a3a 55%, #1f3d8a 100%);
  }

  .sponsor-table { left: 53px; top: 820px; width: 813px; border-collapse: collapse; table-layout: fixed; }
  .sponsor-table th {
    height: 30px; color: #fff; font-family: "Montserrat", sans-serif; font-weight: 600;
    font-size: 17px; letter-spacing: 0.5px;
  }
  .sponsor-table .col-name { background: var(--table-green); }
  .sponsor-table .col-amount { background: var(--table-orange); }
  .sponsor-table .col-paid { background: var(--table-red); }
  .sponsor-table td { height: 31px; border-bottom: 1px solid #fff; }
  .sponsor-table td:nth-child(1) { background: var(--cell-light); }
  .sponsor-table td:nth-child(2) { background: var(--cell-mid); }
  .sponsor-table td:nth-child(3) { background: var(--cell-dark); }

  .partners { left: 53px; top: 1175px; width: 813px; height: 72px; display: flex; align-items: center; justify-content: center; gap: 34px; }
  .partner { display: flex; align-items: center; gap: 10px; font-family: "Open Sans", sans-serif; font-weight: 400; font-size: 20px; }
  .partner--squads { color: var(--partner-purple); }
  .partner--squads .partner-dot { width: 34px; height: 34px; border-radius: 50%; background: var(--partner-purple); }
  .partner--roll { color: var(--partner-green); font-weight: 600; font-size: 30px; }
  .partner-badge { width: 162px; height: 70px; border: 2px solid var(--partner-green); border-radius: 5px; background: #f3f8ef; }
</style>
</head>
<body>
  <main class="form-page">
    <header class="brand">
      <span class="brand-dot"></span>
      <span class="brand-name">Games in Classrooms</span>
    </header>

    <div class="field field--name">
      <div class="field-label">My name</div>
      <div class="field-input">..........................</div>
    </div>
    <div class="field field--class">
      <div class="field-label">My class</div>
      <div class="field-input">..........................</div>
    </div>
    <div class="field field--raised">
      <div class="field-label">I've raised</div>
      <div class="field-input"><span class="currency">£</span>......................</div>
    </div>

    <h1 class="form-title">MY SPONSORSHIP FORM</h1>
    <div class="title-rule"></div>

    <section class="intro">
      <p>I'm going to be taking part in a fun fitness circuit alongside a top GB athlete.</p>
      <p>Please sponsor me to help raise money for new sports equipment for my school and to help support GB athletes to compete for our country and inspire the next generation.</p>
      <p>As a thank you, if I meet these milestones, I'll receive the following prizes:</p>
    </section>

    <div class="milestone milestone--one">
      <div class="wristbands" role="img" aria-label="Photo of blue and red athlete wristbands"></div>
      <div class="milestone-badge"><span class="raise">Raise</span><span class="over">over</span><span class="amount">£5</span></div>
    </div>
    <div class="milestone milestone--two">
      <div class="wristbands" role="img" aria-label="Photo of blue and red athlete wristbands"></div>
      <div class="milestone-badge"><span class="raise">Raise</span><span class="over">over</span><span class="amount">£15</span></div>
    </div>
    <div class="milestone milestone--three">
      <div class="wristbands" role="img" aria-label="Photo of blue and red athlete wristbands"></div>
      <div class="milestone-badge"><span class="raise">Raise</span><span class="over">over</span><span class="amount">£15</span></div>
    </div>
    <div class="plus">+</div>
    <div class="booklet-cover" role="img" aria-label="Signed athlete booklet cover with flag graphics"></div>

    <table class="sponsor-table">
      <thead>
        <tr><th class="col-name">Name</th><th class="col-amount">Amount Sponsored (£)</th><th class="col-paid">Paid? (Please tick)</th></tr>
      </thead>
      <tbody>
        <tr><td></td><td></td><td></td></tr>
        <tr><td></td><td></td><td></td></tr>
        <tr><td></td><td></td><td></td></tr>
        <tr><td></td><td></td><td></td></tr>
        <tr><td></td><td></td><td></td></tr>
        <tr><td></td><td></td><td></td></tr>
        <tr><td></td><td></td><td></td></tr>
        <tr><td></td><td></td><td></td></tr>
        <tr><td></td><td></td><td></td></tr>
        <tr><td></td><td></td><td></td></tr>
      </tbody>
    </table>

    <footer class="partners">
      <div class="partner partner--squads"><span class="partner-dot"></span>After School Squads</div>
      <div class="partner partner--roll">Fresh Roll</div>
      <div class="partner-badge"></div>
    </footer>
  </main>
</body>
</html>
```